Need a corporate background Image with our existing logo for Zoom or Microsoft Teams

Hi,

We require a corporate background image with our existing logo use with Zoom or Microsoft Teams.

Our existing logo is at https://www.halvenrock-systems.com/images/logo_top.png

Thank you.

```html
<!DOCTYPE html>
<html lang="en">
<head>
<meta charset="utf-8">
<title>Halvenrock Systems – Meeting Background</title>
<link href="https://fonts.googleapis.com/css2?family=Poppins:wght@400;600;700&display=swap" rel="stylesheet">
<style>
  :root {
    --brand-blue: #0a6cb6;
    --deep-blue: #045a9c;
    --wave-shadow: #034f8a;
    --panel-light: #ececec;
    --panel-mid: #dcdcdc;
    --text-white: #ffffff;
    --ghost: rgba(255, 255, 255, 0.06);
  }
  html, body {
    margin: 0;
    padding: 0;
    width: 1200px;
    height: 775px;
    overflow: hidden;
    background: var(--brand-blue);
  }
  .backdrop {
    position: relative;
    width: 1200px;
    height: 775px;
    overflow: hidden;
    font-family: "Poppins", sans-serif;
    color: var(--text-white);
  }
  .backdrop__waves {
    position: absolute;
    inset: 0;
    width: 100%;
    height: 100%;
  }
  .ghost-name {
    position: absolute;
    left: 2px;
    bottom: -44px;
    margin: 0;
    font-size: 200px;
    font-weight: 700;
    line-height: 1;
    letter-spacing: -4px;
    color: var(--ghost);
    white-space: nowrap;
  }
  .contact {
    position: absolute;
    left: 77px;
    top: 76px;
  }
  .contact__url {
    margin: 0 0 20px;
    font-size: 22px;
    font-weight: 600;
    letter-spacing: 0.1px;
  }
  .contact__lines {
    margin: 0;
    font-size: 15.5px;
    font-weight: 400;
    line-height: 23px;
  }
  .contact__rule {
    width: 54px;
    height: 2px;
    margin-top: 22px;
    background: var(--text-white);
  }
  .brand {
    position: absolute;
    right: 52px;
    top: 74px;
    display: flex;
    align-items: center;
    gap: 16px;
  }
  .brand__dot {
    width: 52px;
    height: 52px;
    border-radius: 50%;
    background: var(--brand-blue);
  }
  .brand__name {
    margin: 0;
    font-size: 31px;
    font-weight: 700;
    line-height: 32px;
    letter-spacing: -0.5px;
    color: var(--brand-blue);
  }
  .brand__name span {
    display: block;
    font-size: 16px;
    line-height: 22px;
    letter-spacing: 9.5px;
  }
</style>
</head>
<body>
<main class="backdrop">
  <svg class="backdrop__waves" viewBox="0 0 1890 1064" preserveAspectRatio="none" aria-hidden="true">
    <defs>
      <linearGradient id="panelShade" x1="0" y1="0" x2="1" y2="1">
        <stop offset="0" stop-color="var(--panel-mid)"/>
        <stop offset="1" stop-color="var(--panel-light)"/>
      </linearGradient>
    </defs>
    <rect width="1890" height="1064" fill="var(--brand-blue)"/>
    <path class="wave wave--upper" d="M0 0 L380 0 C650 200 900 420 1300 520 C1580 590 1780 590 1890 585 L1890 700 C1600 720 1250 640 900 470 C600 320 300 130 0 60Z" fill="var(--deep-blue)" opacity="0.55"/>
    <path class="wave wave--mid" d="M0 220 C300 380 650 560 1000 640 C1350 720 1650 780 1890 800 L1890 860 C1600 850 1250 800 900 700 C550 600 250 430 0 290Z" fill="var(--deep-blue)" opacity="0.6"/>
    <path class="wave wave--crease" d="M0 300 C280 420 500 460 820 540 C600 500 300 430 0 340Z" fill="var(--wave-shadow)" opacity="0.7"/>
    <path class="wave wave--lower" d="M0 600 C400 620 800 720 1200 820 C1500 900 1750 940 1890 950 L1890 990 C1650 980 1400 950 1150 880 C800 780 400 680 0 660Z" fill="var(--deep-blue)" opacity="0.45"/>
    <path class="panel" d="M837 0 C1150 300 1500 365 1890 345 L1890 0Z" fill="url(#panelShade)"/>
    <path class="panel__stripe" d="M910 0 L985 0 C1250 230 1560 345 1890 328 L1890 340 C1530 352 1220 290 910 0Z" fill="var(--brand-blue)"/>
  </svg>

  <p class="ghost-name" aria-hidden="true">HALVENROCK</p>

  <section class="contact">
    <p class="contact__url">www.halvenrock-systems.com</p>
    <p class="contact__lines">Lorem ipsum<br>consectetuer adipiscing<br>diam nonummy</p>
    <div class="contact__rule"></div>
  </section>

  <div class="brand">
    <div class="brand__dot"></div>
    <p class="brand__name">HALVENROCK<span>SYSTEMS</span></p>
  </div>
</main>
</body>
</html>
```